Design a Flyer

I need a flyer for a Ramadan Camp for kg and 1st graders with the following information on it:
Youth Committee off WLN presents:
Ramadan Camp
Quran, Activities, Arts and crafts, story telling and more!
When:
Session 1: June 7- June 15
Session 2: June 20 - June 29
Monday, Tuesday, Wednesday 3-6 PM
Fees:
Members: $100 per child per session
Non: Members: $130 per child per session
Ages: Kg & 1st grade
Contact info:
Samira Kanzouri 734-2908815
Rula Damsiri 312-5064197
Where:
48210 Pemberly Rd.
Farmington Hills, MI

```html
<!DOCTYPE html>
<html lang="en">
<head>
<meta charset="utf-8">
<title>Ramadan Camp Flyer</title>
<link href="https://fonts.googleapis.com/css2?family=Quicksand:wght@600;700&display=swap" rel="stylesheet">
<style>
  :root {
    --paper: #f3ead2;
    --gold: #b9843b;
    --slate: #4d6186;
    --navy: #1e2a52;
    --blue-text: #3b5381;
    --bar: #233c6b;
    --ink-box: #0d0f17;
    --brand: #8f2323;
  }
  * { margin: 0; padding: 0; box-sizing: border-box; }
  html, body { width: 923px; height: 1200px; overflow: hidden; background: var(--paper); }
  body { font-family: "Quicksand", sans-serif; font-weight: 700; }
  .flyer { position: relative; width: 923px; height: 1200px; background: var(--paper); overflow: hidden; }

  .header { position: absolute; left: 0; top: 0; width: 923px; height: 188px;
    background: linear-gradient(90deg, #f1e8d1 0%, #e9e0c9 60%, #efe6cf 100%); }
  .brand { position: absolute; left: 28px; top: 66px; display: flex; align-items: center; gap: 16px; }
  .brand-dot { width: 52px; height: 52px; border-radius: 50%; background: var(--gold); }
  .brand-name { font-size: 36px; color: var(--brand); font-weight: 700; }
  .ornament { position: absolute; right: 0; top: 0; width: 303px; height: 188px; }

  .photo { position: absolute; left: 0; top: 188px; width: 660px; height: 500px; }

  .headline { position: absolute; left: 540px; top: 238px; width: 380px; text-align: center; white-space: nowrap; }
  .headline .youth { font-size: 52px; line-height: 64px; color: var(--gold); display: block; margin-right: 20px; }
  .headline .line { font-size: 38px; line-height: 57px; color: var(--slate); display: block; }

  .program { position: absolute; right: 40px; top: 568px; text-align: right; font-size: 34px; color: var(--navy); line-height: 47px; }

  .label { color: var(--gold); font-size: 32px; }
  .when { position: absolute; left: 29px; top: 640px; color: var(--blue-text); font-size: 27px; line-height: 37px; }
  .when .label { margin-bottom: 4px; display: block; }
  .fees { position: absolute; left: 538px; top: 740px; color: var(--blue-text); font-size: 25px; line-height: 37.5px; }
  .fees .label { display: block; margin-bottom: 2px; }

  .contact-title { position: absolute; left: 22px; top: 916px; font-size: 46px; color: #1f3c74; }
  .contact-box { position: absolute; left: 7px; top: 972px; width: 584px; height: 114px; background: var(--ink-box);
    color: #fff; font-size: 31px; padding: 10px 0 0 12px; line-height: 46px; }
  .where-tab { position: absolute; left: 613px; top: 1019px; width: 310px; height: 67px; background: var(--bar);
    color: #fff; font-size: 25px; padding: 36px 0 0 46px; }
  .address-bar { position: absolute; left: 7px; top: 1090px; width: 916px; height: 95px; background: var(--bar);
    color: #fff; font-size: 33px; padding: 14px 0 0 100px; }
</style>
</head>
<body>
<div class="flyer">
  <header class="header">
    <div class="brand">
      <span class="brand-dot"></span>
      <span class="brand-name">Westlake Learning Network</span>
    </div>
    <svg class="ornament" viewBox="0 0 303 188" role="img" aria-label="Decorative geometric star ornament in blue and orange">
      <defs>
        <radialGradient id="orn" cx="60%" cy="50%" r="65%">
          <stop offset="0" stop-color="#4a93c9"/>
          <stop offset="0.6" stop-color="#3a79ad"/>
          <stop offset="1" stop-color="#c46a34"/>
        </radialGradient>
      </defs>
      <rect width="303" height="188" fill="url(#orn)"/>
    </svg>
  </header>

  <svg class="photo" viewBox="0 0 660 500" role="img" aria-label="Photo of a young boy wearing a white knit prayer cap">
    <defs>
      <linearGradient id="ph" x1="0" y1="0" x2="1" y2="1">
        <stop offset="0" stop-color="#2f4a2a"/>
        <stop offset="0.5" stop-color="#8a6a55"/>
        <stop offset="1" stop-color="#1c1f2a"/>
      </linearGradient>
    </defs>
    <path d="M0 0 H645 L630 40 L648 70 L600 110 L585 160 L560 200 L530 240 L535 290 L500 330 L470 345 L430 380 L380 370 L350 430 L320 410 L290 460 L260 420 L220 445 L200 405 L150 420 L110 380 L60 395 L20 360 L0 370 Z" fill="url(#ph)"/>
  </svg>

  <div class="headline">
    <span class="youth">Youth</span>
    <span class="line">Committee</span>
    <span class="line">off WLN presents:</span>
    <span class="line">Ramadan Camp</span>
  </div>

  <div class="program">
    <div>Quran ,Activities</div>
    <div>Arts and crafts</div>
    <div>story telling and more!</div>
  </div>

  <section class="when">
    <span class="label">When:</span>
    <div>Session 1:</div>
    <div>June 7- June 15</div>
    <div>Session 2:</div>
    <div>June 20 - June 29</div>
    <div>Monday, Tuesday</div>
    <div>Wednesday 3-6 PM</div>
  </section>

  <section class="fees">
    <span class="label">Fees:</span>
    <div>Members:</div>
    <div>$100 per child per session</div>
    <div>Non: Members:</div>
    <div>$130 per child per session</div>
    <div>Ages: Kg &amp; 1st grade</div>
  </section>

  <h2 class="contact-title">Contact info:</h2>
  <div class="contact-box">
    <div>Samira Kanzouri 734-2908815</div>
    <div>Rula Damsiri 312-5064197</div>
  </div>

  <div class="where-tab">Where:</div>
  <div class="address-bar">48210 Pemberly Rd. Farmington Hills, MI</div>
</div>
</body>
</html>
```